Business Card Design Project - KLB

I am looking for a more sophisticated card design for my company,
"The Kestrel Bureau"

We are a consultancy focused on strategy and change in Associations and professional organisations.

I am a lawyer and psychologist with a PhD and so am looking for something that communicates seriousness and credibility but also quirky creative solutions for strategic problems, which is my field of speciality.

I am looking for something that is quietly spoken, rather than loud colours ('credible' and 'creative' are the two adjectives that I think of as competing here).

I particularly like an embossed card style - heavy white card with plain white or white and black or white and grey text.

The key logo image for the company is a question mark and I am open to suggestions and ideas on design.

I have attached a file that includes a couple of styles that have caught my eye and my thoughts on them. Hopefully they communicate what I'm looking for.
Updates

Thank you for all the great suggestions and designs.

I really appreciated the effort and creative energy you put into your designs. I have now closed the project after selecting a design and advising the successful designer of the card that I am happy with.

Regards

Target Market(s)

Organisations (CEO's and Boards), Governments, Legal professionals, Membership Associations and aspiring professionals.

Industry/Entity Type

Lawyer

Requirements
Must have
• The key logo element is a question mark (?) and this needs to be incorporated.

Embossed style - cut outs or other design ideas interest me too.

The attached file has a number of sample ideas and comments on each one that I like.
Should not have
• I like crisp, modern fonts (Myriads etc...) and do not like embellished fonts or Times etc...

```html
<!DOCTYPE html>
<html lang="en">
<head>
<meta charset="utf-8">
<title>The Kestrel Bureau – Business Card, Option 1 Back</title>
<link rel="stylesheet" href="https://fonts.googleapis.com/css2?family=PT+Sans:ital,wght@0,400;1,400&family=Saira+Semi+Condensed:wght@400&family=Arimo&display=swap">
<style>
  :root {
    --sheet-bg: #ffffff;
    --sheet-border: #c8c8c8;
    --heading-ink: #1a1a1a;
    --card-plum: #761850;
    --card-ink: #f6eef3;
    --band-cream: #f2ecd8;
    --card-shadow: rgba(0, 0, 0, 0.18);
  }
  html, body {
    margin: 0;
    padding: 0;
    overflow: hidden;
    background: var(--sheet-bg);
  }
  .presentation-sheet {
    position: relative;
    width: 1200px;
    height: 874px;
    box-sizing: border-box;
    border: 1px solid var(--sheet-border);
    background: var(--sheet-bg);
    overflow: hidden;
  }
  .option-heading {
    position: absolute;
    left: 32px;
    top: 56px;
    margin: 0;
    font: 400 37px/1 "Arimo", Arial, sans-serif;
    color: var(--heading-ink);
  }
  .business-card {
    position: absolute;
    left: 251px;
    top: 226px;
    width: 698px;
    height: 421px;
    background: var(--card-plum);
    box-shadow: 0 0 4px var(--card-shadow);
    color: var(--card-ink);
    font-family: "PT Sans", "Myriad Pro", sans-serif;
  }
  .holder-name {
    position: absolute;
    left: 0;
    width: 700px;
    top: 21px;
    margin: 0;
    text-align: center;
    font-style: italic;
    font-size: 17px;
    letter-spacing: 0.3px;
  }
  .brand-mark {
    position: absolute;
    left: 230px;
    top: 100px;
    width: 145px;
    text-align: center;
    font-size: 68px;
    line-height: 1;
    color: #ffffff;
  }
  .company-name {
    position: absolute;
    left: 98px;
    top: 240px;
    margin: 0;
    font-family: "Saira Semi Condensed", "Eurostile", sans-serif;
    font-size: 28px;
    line-height: 1;
    letter-spacing: 0.2px;
  }
  .tagline-band {
    position: absolute;
    left: 0;
    top: 272px;
    width: 100%;
    height: 27px;
    background: var(--band-cream);
  }
  .tagline {
    position: absolute;
    right: 99px;
    top: 2px;
    margin: 0;
    font-style: italic;
    font-size: 18px;
    line-height: 22px;
    color: var(--card-plum);
    letter-spacing: 0.3px;
  }
  .contact-block {
    position: absolute;
    left: 0;
    width: 700px;
    top: 332px;
    margin: 0;
    text-align: center;
    font-style: normal;
    font-size: 17px;
    line-height: 25px;
  }
  .contact-block .gap { display: inline-block; width: 22px; }
</style>
</head>
<body>
  <main class="presentation-sheet">
    <h1 class="option-heading">Option 1- back (color choice)</h1>

    <section class="business-card" aria-label="Business card back">
      <p class="holder-name">Dr. Mara Ellison, Director</p>
      <div class="brand-mark">KLB</div>
      <h2 class="company-name">THE KESTREL BUREAU</h2>
      <div class="tagline-band">
        <p class="tagline">all questions ... answered</p>
      </div>
      <address class="contact-block">
        P. O. Box 4318, Linden Grove, Harbourton, Australia<br>
        M : +61400 127354<span class="gap"></span>P: + 61290046518<br>
        E: mara@kestrelbureau.com.au
      </address>
    </section>
  </main>
</body>
</html>
```